Vorlan cards

I am in the auto motive, transportation business I would like a business card that is Something cool, modern edgy, having to do with car culture. I offer towing service for high and exotic cars. I also provide towing for collisions and car accidents. I offer open and enclosed transport nationwide.

Target Market(s)

Car culture people high end auto collectors

Industry/Entity Type

Towing car carrier

Contact Information for Business Card

My company colors black yellow and silver

Font styles to use
Serif

```html
<!DOCTYPE html>
<html lang="en">
<head>
<meta charset="utf-8">
<title>Vorlan Transportation – Business Cards</title>
<link rel="stylesheet" href="https://fonts.googleapis.com/css2?family=Arvo:wght@400;700&family=Lato:wght@400&display=swap">
<style>
  :root {
    --backdrop: #3a3b3d;
    --silver-light: #e4e5e7;
    --silver-mid: #cfd0d3;
    --silver-dark: #b6b8bb;
    --ink: #0d0d0d;
    --ink-soft: #2a2a2a;
    --yellow: #f7dc5c;
  }
  * { box-sizing: border-box; margin: 0; padding: 0; }
  html, body { width: 1200px; height: 800px; overflow: hidden; }
  body {
    background: var(--backdrop);
    display: flex;
    flex-direction: column;
    align-items: center;
    justify-content: center;
    gap: 48px;
  }
  .card {
    position: relative;
    width: 560px;
    height: 320px;
    border-radius: 22px;
    overflow: hidden;
    background: linear-gradient(160deg, var(--silver-light) 0%, var(--silver-mid) 55%, var(--silver-dark) 100%);
    box-shadow: 0 10px 24px rgba(0,0,0,0.35);
  }

  /* Contact side */
  .card-contact .identity {
    position: absolute;
    left: 36px;
    bottom: 56px;
    width: 250px;
    color: var(--ink);
    z-index: 1;
  }
  .identity .person-name {
    font-family: "Arvo", serif;
    font-weight: 400;
    font-size: 22px;
    letter-spacing: 1px;
    line-height: 1;
    white-space: nowrap;
  }
  .identity .person-role {
    font-family: "Lato", sans-serif;
    font-size: 13px;
    letter-spacing: 0.5px;
    color: var(--ink-soft);
    margin-top: 6px;
  }
  .identity .accent-rule {
    width: 70px;
    height: 5px;
    background: var(--yellow);
    margin: 10px 0 12px 26px;
  }
  .contact-list { list-style: none; }
  .contact-list li {
    display: flex;
    align-items: center;
    gap: 10px;
    font-family: "Lato", sans-serif;
    font-size: 13px;
    line-height: 1.55;
    color: var(--ink);
    white-space: nowrap;
  }
  .contact-list li.phone { font-size: 17px; }
  .contact-list svg { width: 12px; height: 12px; flex: none; }

  .truck-art {
    position: absolute;
    right: 0;
    top: 0;
    width: 250px;
    height: 100%;
    background: linear-gradient(120deg, #111 0%, #000 70%, #1a1a1a 100%);
    border-top-left-radius: 90px 120px;
    border-bottom-left-radius: 30px;
  }

  /* Logo side */
  .card-brand {
    display: flex;
    align-items: center;
    justify-content: center;
  }
  .brand-lockup {
    display: flex;
    align-items: center;
    gap: 12px;
  }
  .brand-lockup .brand-square {
    flex: none;
    width: 20px;
    height: 20px;
    background: var(--yellow);
  }
  .brand-lockup .brand-name {
    font-family: "Arvo", serif;
    font-weight: 700;
    font-size: 28px;
    color: var(--ink);
    letter-spacing: 1px;
    white-space: nowrap;
  }
</style>
</head>
<body>

  <section class="card card-contact" aria-label="Business card, contact side">
    <div class="identity">
      <h1 class="person-name">DALE WHITMORE</h1>
      <p class="person-role">Managing Director</p>
      <div class="accent-rule"></div>
      <ul class="contact-list">
        <li class="phone">
          <svg viewBox="0 0 24 24" aria-hidden="true"><path fill="#0d0d0d" d="M6.6 10.8a15.1 15.1 0 0 0 6.6 6.6l2.2-2.2a1 1 0 0 1 1-.25 11.4 11.4 0 0 0 3.6.57 1 1 0 0 1 1 1V20a1 1 0 0 1-1 1A17 17 0 0 1 3 4a1 1 0 0 1 1-1h3.5a1 1 0 0 1 1 1c0 1.25.2 2.45.57 3.57a1 1 0 0 1-.25 1z"/></svg>
          123-456-7890
        </li>
        <li>
          <svg viewBox="0 0 24 24" aria-hidden="true"><rect x="2" y="5" width="20" height="14" rx="1" fill="#0d0d0d"/><path d="M3 6l9 7 9-7" stroke="#e4e5e7" stroke-width="2" fill="none"/></svg>
          whitmore@yourwebsite.com
        </li>
        <li>
          <svg viewBox="0 0 24 24" aria-hidden="true"><circle cx="12" cy="12" r="10" fill="#0d0d0d"/><path d="M2 12h20M12 2c3 3 3 17 0 20M12 2c-3 3-3 17 0 20" stroke="#e4e5e7" stroke-width="1.5" fill="none"/></svg>
          www.yourwebsite.com
        </li>
      </ul>
    </div>
    <div class="truck-art" role="img" aria-label="Large black illustration of a flatbed tow truck with a yellow accent"></div>
  </section>

  <section class="card card-brand" aria-label="Business card, brand side">
    <div class="brand-lockup">
      <span class="brand-square" aria-hidden="true"></span>
      <span class="brand-name">VORLAN TRANSPORTATION</span>
    </div>
  </section>

</body>
</html>
```